Creative Brief
tarnell financial llc .com
tarnellfinancial.example
I need double sided standard sized Business Card [3.5" x 2"]
just keep logo in mind
Professional
Dale Tarnell
President
4178 E. K Ave.
Greeley, CO 80219
dale@tarnellfinancial.example
I was in a logo contest, please utilize that design
as you see fit

```html
<!DOCTYPE html>
<html lang="en">
<head>
<meta charset="utf-8">
<title>Tarnell Financial Stationery</title>
<link href="https://fonts.googleapis.com/css2?family=Open+Sans:wght@400;600;700&display=swap" rel="stylesheet">
<style>
:root{
  --bg:#e9ebec;
  --paper:#ffffff;
  --blue:#1d5f9c;
  --blue-dark:#103f6e;
  --blue-light:#3d8fcf;
  --green:#7ab648;
  --green-light:#a6d06f;
  --ink:#2f3a45;
  --muted:#8a949c;
  --wash:#eef2f5;
}
*{box-sizing:border-box;margin:0;padding:0}
html,body{width:1200px;height:446px;overflow:hidden;background:var(--bg);font-family:"Open Sans",Arial,sans-serif;color:var(--ink)}
.canvas{position:relative;width:1200px;height:446px}
.piece{position:absolute;background:var(--paper);box-shadow:0 2px 6px rgba(0,0,0,.18);overflow:hidden}
.label{position:absolute;font-size:7px;color:var(--muted);text-align:center}
.brand{display:flex;align-items:center;gap:4px;font-weight:700;color:var(--blue);white-space:nowrap}
.brand .mark{background:var(--blue);display:block}
.swoosh{position:absolute;display:block}
.wash{position:absolute;border-radius:50%;background:radial-gradient(circle,var(--wash) 0%,rgba(238,242,245,0) 70%)}
/* business cards */
.card{width:130px;height:74px}
.card-front{left:19px;top:149px}
.card-back-blue{left:19px;top:240px;background:linear-gradient(135deg,var(--blue-light),var(--blue-dark))}
.card-back-white{left:19px;top:336px}
.card-name{position:absolute;left:62px;top:12px;font-size:5px;line-height:1.5}
.card-name b{font-size:6px;color:var(--blue)}
.card-lines{position:absolute;left:62px;top:32px;font-size:4px;line-height:1.6;color:var(--ink)}
.card-back-blue .card-lines{left:70px;top:24px;color:#fff}
.card-back-white .card-lines{left:70px;top:24px}
.card-brand{position:absolute;left:8px;top:14px;font-size:5px}
.card-brand .mark{width:7px;height:7px}
.card-back-blue .brand{color:#fff}
.card-back-blue .brand .mark{background:#fff}
/* letterheads */
.letterhead{width:276px;height:399px;top:14px}
.lh-1{left:240px}
.lh-2{left:557px}
.lh-brand{position:absolute;top:18px;font-size:8px}
.lh-1 .lh-brand{left:112px}
.lh-2 .lh-brand{left:112px}
.lh-brand .mark{width:10px;height:10px}
.lh-footer{position:absolute;bottom:16px;left:0;right:0;text-align:center;font-size:4.5px;color:var(--muted)}
/* envelopes */
.envelope{left:864px;width:324px;height:92px}
.env-green{top:34px;background:linear-gradient(180deg,var(--green-light),var(--green))}
.env-blue{top:112px;background:linear-gradient(180deg,var(--blue-light),var(--blue))}
.env-plain{top:196px}
.env-front{top:286px}
.env-flap{position:absolute;left:0;top:0}
.env-brand{position:absolute;font-size:6px}
.env-brand .mark{width:8px;height:8px}
.env-green .env-brand,.env-blue .env-brand{color:#fff;left:140px;top:10px}
.env-green .env-brand .mark,.env-blue .env-brand .mark{background:#fff}
.env-plain .env-brand{left:140px;top:46px}
.env-front .env-brand{left:12px;top:12px}
.env-addr{position:absolute;left:12px;top:26px;font-size:4px;line-height:1.5;color:var(--muted)}
</style>
</head>
<body>
<div class="canvas">

  <!-- business cards -->
  <div class="piece card card-front">
    <svg class="swoosh" width="130" height="74" viewBox="0 0 130 74"><path d="M0 74 L0 56 Q40 70 90 74 Z" fill="var(--blue)"/><path d="M0 56 Q40 68 90 74 L70 74 Q30 68 0 61 Z" fill="var(--green)"/></svg>
    <div class="brand card-brand"><span class="mark"></span>tarnell financial</div>
    <div class="card-name"><b>Dale Tarnell</b><br>President</div>
    <div class="card-lines">4178 E. K Ave.<br>Greeley, CO 80219<br>dale@tarnellfinancial.example<br>tarnellfinancial.example</div>
  </div>
  <div class="label" style="left:19px;top:226px;width:130px">Front Card</div>

  <div class="piece card card-back-blue">
    <div class="wash" style="left:-20px;top:-10px;width:90px;height:90px;opacity:.25"></div>
    <div class="brand card-brand"><span class="mark"></span>tarnell</div>
    <div class="card-lines">• Financial Planning<br>• Retirement Income<br>• Investment Advice</div>
  </div>
  <div class="label" style="left:19px;top:321px;width:130px">Back Card Option #1</div>

  <div class="piece card card-back-white">
    <div class="wash" style="left:-20px;top:-10px;width:90px;height:90px"></div>
    <div class="brand card-brand"><span class="mark"></span>tarnell</div>
    <div class="card-lines">• Financial Planning<br>• Retirement Income<br>• Investment Advice</div>
  </div>
  <div class="label" style="left:19px;top:418px;width:130px">Back Card Option #2</div>

  <!-- letterheads -->
  <div class="piece letterhead lh-1">
    <svg class="swoosh" width="276" height="399" viewBox="0 0 276 399">
      <path d="M190 0 Q250 6 276 40 L276 0 Z" fill="var(--blue)"/>
      <path d="M180 0 Q246 10 276 48 L276 40 Q250 6 190 0 Z" fill="var(--green)"/>
      <path d="M0 340 Q20 385 80 399 L0 399 Z" fill="var(--blue)"/>
      <path d="M0 332 Q22 384 90 399 L80 399 Q20 385 0 340 Z" fill="var(--green)"/>
    </svg>
    <div class="wash" style="left:20px;top:90px;width:220px;height:220px" role="img" aria-label="Faint brand backdrop"></div>
    <div class="brand lh-brand"><span class="mark"></span>tarnell financial</div>
    <div class="lh-footer">4178 E. K Ave. · Greeley, CO 80219 · tarnellfinancial.example</div>
  </div>
  <div class="label" style="left:240px;top:418px;width:276px">Letterhead Option #1</div>

  <div class="piece letterhead lh-2">
    <svg class="swoosh" width="276" height="399" viewBox="0 0 276 399">
      <path d="M200 0 Q255 4 276 30 L276 0 Z" fill="var(--blue)"/>
      <path d="M276 370 Q240 392 200 399 L276 399 Z" fill="var(--blue)"/>
      <path d="M276 362 Q236 390 190 399 L200 399 Q240 392 276 370 Z" fill="var(--green)"/>
    </svg>
    <div class="wash" style="left:20px;top:90px;width:220px;height:220px" role="img" aria-label="Faint brand backdrop"></div>
    <div class="brand lh-brand"><span class="mark"></span>tarnell financial</div>
    <div class="lh-footer">4178 E. K Ave. · Greeley, CO 80219 · tarnellfinancial.example</div>
  </div>
  <div class="label" style="left:557px;top:418px;width:276px">Letterhead Option #2</div>

  <!-- envelopes -->
  <div class="piece envelope env-green">
    <svg class="env-flap" width="324" height="92" viewBox="0 0 324 92"><path d="M0 0 L162 40 L324 0" fill="none" stroke="rgba(255,255,255,.5)" stroke-width="1"/></svg>
    <div class="brand env-brand"><span class="mark"></span>tarnell financial</div>
  </div>
  <div class="piece envelope env-blue">
    <svg class="env-flap" width="324" height="92" viewBox="0 0 324 92"><path d="M0 0 L162 40 L324 0" fill="none" stroke="rgba(255,255,255,.5)" stroke-width="1"/></svg>
    <div class="brand env-brand"><span class="mark"></span>tarnell financial</div>
  </div>
  <div class="piece envelope env-plain">
    <svg class="env-flap" width="324" height="92" viewBox="0 0 324 92"><path d="M0 0 L162 40 L324 0" fill="none" stroke="#d6dbe0" stroke-width="1"/></svg>
    <div class="brand env-brand"><span class="mark"></span>tarnell financial</div>
  </div>
  <div class="piece envelope env-front">
    <svg class="swoosh" width="324" height="92" viewBox="0 0 324 92">
      <path d="M324 50 Q300 84 240 92 L324 92 Z" fill="var(--blue)"/>
      <path d="M324 42 Q296 82 228 92 L240 92 Q300 84 324 50 Z" fill="var(--green)"/>
    </svg>
    <div class="brand env-brand"><span class="mark"></span>tarnell financial</div>
    <div class="env-addr">4178 E. K Ave.<br>Greeley, CO 80219</div>
  </div>
  <div class="label" style="left:864px;top:384px;width:324px">Envelope Front &amp; Back</div>

</div>
</body>
</html>
```